Content processing platform needs a new front page design

We need a new front page design for Plumtext.com. Plumtext.com is a free content processing platform that helps online businesses and freelancers scale their production of content and translation. See pdf for a mockup on what we wish to communicate and layout of the front page. The final design should communicate scalability/growth and we hope to see a design where the user clicks one of the links for iGaming, e-shop, agency in the middle. 60% of our traffic is from mobile devices..

Number of Pages Required

1 page

Font styles to use
Other font styles liked:
• open sans

```html
<!DOCTYPE html>
<html lang="en">
<head>
<meta charset="utf-8">
<title>Plumtext.com – Scale your content production</title>
<link href="https://fonts.googleapis.com/css2?family=Open+Sans:ital,wght@0,400;0,600;0,700;1,400&family=Roboto+Condensed:wght@400;700&display=swap" rel="stylesheet">
<style>
:root{
  --pink:#f2336e;
  --blue:#1aa6ea;
  --navy:#1c2a36;
  --dark:#2f3133;
  --footer:#252627;
  --footer-deep:#1b1c1d;
  --grey-bg:#f1f2f4;
  --box-bg:#e9eaec;
  --text:#2b2b2b;
  --muted:#6d7278;
  --white:#ffffff;
}
*{box-sizing:border-box;margin:0;padding:0}
html,body{width:1200px;height:3468px;overflow:hidden}
body{font-family:"Open Sans",Arial,sans-serif;color:var(--text);background:var(--white);position:relative}
.head{font-family:"Roboto Condensed","Arial Narrow",sans-serif;font-weight:700;text-transform:uppercase}
section,header,footer,nav{position:absolute;left:0;width:1200px}

/* top bar */
.topbar{top:0;height:80px;display:flex;align-items:center;padding:0 80px 0 64px}
.brand{display:flex;align-items:center;gap:10px;font-weight:700;font-size:30px;color:var(--pink)}
.brand-dot{width:26px;height:26px;background:var(--navy);border-radius:4px}
.topbar-actions{margin-left:auto;display:flex;gap:14px}
.btn{display:inline-block;font-weight:700;font-size:13px;color:var(--white);padding:11px 20px;text-transform:uppercase;letter-spacing:.3px}
.btn-pink{background:var(--pink)}
.btn-blue{background:var(--blue)}
.btn-outline{border:2px solid var(--text);color:var(--text);background:transparent;padding:9px 18px}
.mainnav{top:80px;height:40px;background:var(--navy);display:flex;justify-content:center;align-items:center;gap:36px}
.mainnav a{color:var(--white);font-size:13px;font-weight:600;text-transform:uppercase;text-decoration:none}

/* hero */
.hero{top:120px;height:430px;background:var(--white)}
.hero-title{position:absolute;left:64px;top:44px;width:570px;font-size:30px;line-height:36px;color:var(--text)}
.hero-cols{position:absolute;left:64px;top:172px;display:flex;gap:70px}
.hero-col h3{font-size:20px;margin-bottom:8px}
.hero-col p{font-size:13px;line-height:19px;color:var(--muted);width:200px;margin-bottom:18px}
.hero-cta{position:absolute;left:64px;top:340px;display:flex;gap:24px}
.hero-cta .btn{padding:14px 30px}
.hero-devices{position:absolute;left:660px;top:30px;width:500px;height:370px;border-radius:8px;background:linear-gradient(160deg,#eef2f5,#c9d1d8 60%,#9aa4ad)}

/* latest */
.latest{top:550px;height:110px;background:var(--dark);color:var(--white);text-align:center;padding-top:30px}
.latest h2{font-size:24px}
.latest p{font-size:14px;color:#c9cbcd;margin-top:6px}

/* scale choices */
.scale{top:660px;height:300px;text-align:center}
.scale h2{font-size:34px;padding-top:48px}
.choices{position:absolute;top:122px;left:0;width:1200px;display:flex}
.choice{flex:1;display:flex;flex-direction:column;align-items:center}
.choice-ring{width:88px;height:88px;border-radius:50%;border:5px solid var(--pink);display:flex;align-items:center;justify-content:center;background:var(--white)}
.choice-label{margin-top:28px;font-size:15px}
.clients{top:960px;height:120px;background:var(--grey-bg);display:flex;justify-content:center;align-items:center;gap:24px}
.client{width:200px;height:80px;background:var(--white);display:flex;align-items:center;justify-content:center;gap:10px;font-weight:700;font-size:26px;color:var(--navy)}
.client-mark{width:16px;height:16px;background:var(--navy)}

/* benefits */
.benefits{top:1120px;height:420px;background:var(--blue);display:flex;justify-content:center;gap:40px;padding-top:40px}
.benefit{width:330px;height:340px;border:3px solid rgba(255,255,255,.8);color:var(--white);text-align:center;padding:30px 28px}
.benefit-art{width:120px;height:120px;margin:0 auto 20px;border-radius:50%;background:linear-gradient(150deg,#ffffff,#d9eef9)}
.benefit h3{font-size:24px;margin-bottom:10px}
.benefit p{font-size:13px;line-height:19px}

/* signup */
.signup{top:1590px;height:250px;background:var(--pink);color:var(--white);text-align:center;padding-top:56px}
.signup h2{font-size:58px;line-height:60px}
.signup .sub{font-size:15px;letter-spacing:1px;opacity:.85;margin-top:4px}
.signup .btn{margin-top:26px;border:2px solid var(--white);padding:13px 26px;font-size:15px}

/* dashboard */
.dashboard{top:1860px;height:400px}
.dashboard-shot{position:absolute;left:190px;top:20px;width:820px;height:360px;border-radius:10px;background:linear-gradient(180deg,#3a3d40,#cfd5da 12%,#eef2f5 70%,#b9c0c6)}

/* solutions */
.solutions{top:2280px;height:240px;display:flex;justify-content:center;gap:22px}
.solution{width:330px;height:200px;background:var(--box-bg);border-bottom:6px solid var(--pink);text-align:center;padding:46px 24px 0}
.solution h3{font-size:18px;margin-bottom:14px}
.solution p{font-size:13px;line-height:19px;color:var(--muted)}

/* testimonial */
.testimonial{top:2560px;height:250px;background:var(--blue);color:var(--white);text-align:center}
.avatar{position:absolute;left:545px;top:-48px;width:110px;height:110px;border-radius:50%;border:5px solid var(--white);background:linear-gradient(160deg,#d8d2cc,#8a8580)}
.quote{position:absolute;left:200px;top:90px;width:800px;font-size:13px;line-height:20px;font-style:italic}
.quote-name{position:absolute;left:0;width:1200px;top:186px;font-size:14px;font-weight:600}
.arrow{position:absolute;top:110px;width:40px;height:40px;border-radius:50%;border:2px solid var(--white);display:flex;align-items:center;justify-content:center}
.arrow-left{left:120px}.arrow-right{right:120px}

/* app */
.app{top:2850px;height:310px}
.app-photo{position:absolute;left:20px;top:30px;width:260px;height:260px;border-radius:50%;background:linear-gradient(150deg,#e7e9ea,#9ca3a8 55%,#4b5258)}
.app-text{position:absolute;left:320px;top:50px;width:820px}
.app-text h2{font-size:44px;line-height:48px}
.app-text h3{font-family:"Open Sans",Arial,sans-serif;font-size:28px;font-weight:400;margin-bottom:16px}
.app-text p{font-size:13px;line-height:20px;color:var(--muted)}
.stores{display:flex;gap:16px;margin-top:22px}
.store{width:150px;height:46px;border-radius:8px;background:#111}

/* footer */
.footer{top:3160px;height:308px;background:var(--footer);color:#bfc2c5}
.footer-cols{position:absolute;left:64px;top:36px;width:1072px;display:flex;justify-content:space-between}
.footer-col{width:230px}
.footer-col h4{font-size:16px;color:var(--white);padding-bottom:8px;border-bottom:2px solid var(--pink);display:inline-block;margin-bottom:16px}
.footer-col li{list-style:none;font-size:12px;line-height:22px}
.footer-map{width:230px;height:140px;background:linear-gradient(135deg,#e6e2d6,#cfd8c8)}
.socials{display:flex;gap:8px;margin-top:14px}
.social{width:28px;height:28px;background:#3a3c3e}
.copyright{position:absolute;left:0;bottom:0;width:1200px;height:46px;background:var(--footer-deep);font-size:12px;text-align:center;line-height:46px;color:#8d9094}
</style>
</head>
<body>

<header class="topbar">
  <div class="brand"><span class="brand-dot"></span>Plumtext</div>
  <div class="topbar-actions">
    <span class="btn btn-pink">Scale your business</span>
    <span class="btn btn-blue">Become a freelancer</span>
  </div>
</header>
<nav class="mainnav">
  <a>Products ▾</a><a>Apps ▾</a><a>Prices</a><a>Blog</a><a>Help Center</a>
</nav>

<section class="hero">
  <h1 class="hero-title head">Scale your production of content and translation with our free platform.</h1>
  <div class="hero-cols">
    <div class="hero-col">
      <h3 class="head">Business</h3>
      <p>Scale your online content. Let 1000s of writers and translators work for you.</p>
      <span class="btn btn-outline">Learn more</span>
    </div>
    <div class="hero-col">
      <h3 class="head">Freelance</h3>
      <p>Freelance when you want. Get paid for every word you write or translate.</p>
      <span class="btn btn-outline">Learn more</span>
    </div>
  </div>
  <div class="hero-cta">
    <span class="btn btn-pink">Sign up to scale content</span>
    <span class="btn btn-blue">Sign up to freelance</span>
  </div>
  <div class="hero-devices" role="img" aria-label="Laptop, desktop, tablet and phone showing the platform dashboard"></div>
</section>

<section class="latest">
  <h2 class="head">Latest content from the crowd</h2>
  <p>Elena wrote the text Lucky Falcon Slot in English 15 minutes ago.</p>
</section>

<section class="scale">
  <h2 class="head">What do you want to scale?</h2>
  <div class="choices">
    <div class="choice">
      <div class="choice-ring"><svg width="44" height="30" viewBox="0 0 44 30" fill="none" stroke="#2b2b2b" stroke-width="3"><rect x="2" y="4" width="40" height="22" rx="11"/><path d="M12 10v10M7 15h10"/><circle cx="30" cy="12" r="2"/><circle cx="34" cy="18" r="2"/></svg></div>
      <div class="choice-label head">iGaming</div>
    </div>
    <div class="choice">
      <div class="choice-ring"><svg width="40" height="36" viewBox="0 0 40 36" fill="none" stroke="#2b2b2b" stroke-width="3"><path d="M2 4h6l5 20h20l4-14H11"/><circle cx="15" cy="31" r="3"/><circle cx="31" cy="31" r="3"/></svg></div>
      <div class="choice-label head">eShop</div>
    </div>
    <div class="choice">
      <div class="choice-ring"><svg width="40" height="40" viewBox="0 0 40 40" fill="none" stroke="#2b2b2b" stroke-width="3"><circle cx="20" cy="20" r="17"/><ellipse cx="20" cy="20" rx="7" ry="17"/><path d="M3 20h34"/></svg></div>
      <div class="choice-label head">New markets</div>
    </div>
    <div class="choice">
      <div class="choice-ring"><svg width="40" height="40" viewBox="0 0 40 40" fill="none" stroke="#2b2b2b" stroke-width="3"><circle cx="20" cy="20" r="17"/><circle cx="20" cy="20" r="10"/><circle cx="20" cy="20" r="3" fill="#2b2b2b"/></svg></div>
      <div class="choice-label head">Agency</div>
    </div>
    <div class="choice">
      <div class="choice-ring"><svg width="36" height="40" viewBox="0 0 36 40" fill="none" stroke="#2b2b2b" stroke-width="3"><circle cx="18" cy="12" r="9"/><path d="M3 38c0-9 7-15 15-15s15 6 15 15"/></svg></div>
      <div class="choice-label head">Professional freelancing</div>
    </div>
  </div>
</section>

<section class="clients">
  <div class="client"><span class="client-mark"></span>Northfield</div>
  <div class="client">Greenhill</div>
  <div class="client">Brickhome</div>
  <div class="client">Dalton</div>
  <div class="client">Visitra</div>
</section>

<section class="benefits">
  <div class="benefit">
    <div class="benefit-art" role="img" aria-label="Illustration of a piggy bank with coins"></div>
    <h3 class="head">50% Cheaper</h3>
    <p>Online businesses using Plumtext save on average 50% on their internal and external costs for content and translation.</p>
  </div>
  <div class="benefit">
    <div class="benefit-art" role="img" aria-label="Illustration of a writer working at a computer"></div>
    <h3 class="head">10X Faster</h3>
    <p>With 1000s of freelance writers and translators, Plumtext scales your content production ten times faster.</p>
  </div>
  <div class="benefit">
    <div class="benefit-art" role="img" aria-label="Illustration of automated workflow with a rocket"></div>
    <h3 class="head">10X Faster</h3>
    <p>Plumtext features 100% automated workflows including plagiarism scans and uploading texts to your site.</p>
  </div>
</section>

<section class="signup">
  <h2 class="head">Sign up now</h2>
  <div class="sub head">Try it for yourself – without charge</div>
  <span class="btn">Get started – it's free!</span>
</section>

<section class="dashboard">
  <div class="dashboard-shot" role="img" aria-label="Laptop showing the Plumtext dashboard with statistics and a bar chart"></div>
</section>

<section class="solutions">
  <div class="solution">
    <h3 class="head">Ecommerce content</h3>
    <p>We have expert solutions for multilingual eShops with more than 1000 products.</p>
  </div>
  <div class="solution">
    <h3 class="head">Gaming content</h3>
    <p>We provide content &amp; translation to the world's leading operators and affiliates.</p>
  </div>
  <div class="solution">
    <h3 class="head">Self-service content &amp; translations</h3>
    <p>We have expert solutions for multilingual eShops with more than 1000 products.</p>
  </div>
</section>

<section class="testimonial">
  <div class="avatar" role="img" aria-label="Portrait photo of the customer"></div>
  <div class="arrow arrow-left"><svg width="14" height="14" viewBox="0 0 14 14"><path d="M9 2L4 7l5 5" fill="none" stroke="#fff" stroke-width="2"/></svg></div>
  <div class="arrow arrow-right"><svg width="14" height="14" viewBox="0 0 14 14"><path d="M5 2l5 5-5 5" fill="none" stroke="#fff" stroke-width="2"/></svg></div>
  <p class="quote">"Plumtext helped us scale our content production across eight new markets in just a few months. The writers are skilled, the workflow is simple and our costs dropped by half. We publish more content than ever, and the quality keeps getting better with every order we place."</p>
  <div class="quote-name">Jonas Berg, CEO</div>
</section>

<section class="app">
  <div class="app-photo" role="img" aria-label="Hand holding a phone running the Plumtext app"></div>
  <div class="app-text">
    <h2 class="head">Plumtext App</h2>
    <h3>Why Plumtext App for e-commerce?</h3>
    <p>You probably noticed that we wrote Plumtext in the text above. The reason we wrote it is that many people search for content services and find us. We help online businesses write and translate product texts, category pages and guides at scale, so they can reach new customers in every market they enter.</p>
    <div class="stores">
      <div class="store" role="img" aria-label="App store download badge"></div>
      <div class="store" role="img" aria-label="Play store download badge"></div>
    </div>
  </div>
</section>

<footer class="footer">
  <div class="footer-cols">
    <div class="footer-col">
      <h4 class="head">Plumtext</h4>
      <ul><li>About us</li><li>Jobs</li><li>Contact</li><li>Terms of service</li><li>Privacy policy</li><li>Sitemap</li></ul>
    </div>
    <div class="footer-col">
      <h4 class="head">Resources</h4>
      <ul><li>Plumtext affiliate</li><li>Partners</li><li>Freelancer resources</li><li>Business resources</li><li>FAQ</li></ul>
    </div>
    <div class="footer-col">
      <h4 class="head">Get in location</h4>
      <div class="footer-map" role="img" aria-label="Map showing the office location"></div>
    </div>
    <div class="footer-col">
      <h4 class="head">Contact info</h4>
      <ul><li>Harbour Street 12</li><li>411 04 Lakeside, Sweden</li><li>+46 00 000 00 00</li><li>hello@plumtext.com</li></ul>
      <div class="socials"><span class="social"></span><span class="social"></span><span class="social"></span><span class="social"></span></div>
    </div>
  </div>
  <div class="copyright">© 2024 Plumtext.com. All rights reserved.</div>
</footer>

</body>
</html>
```